Business Card Design Project

I am a psychotherapist, counselor and expressive arts therapist (means I use every art form imaginable in the service of healing). I'm just starting out in private practice in San Francisco, CA. I work with individual adults, children and families. I'd like the card to mirror the simplicity and color palate of my website. I also would love if there is a symbol, image of fire, flame or spark (that is warming, not frightening).

Check out my website: www.lorabeckettmft.com

I want the cards to be printed in letter press so please keep that in mind!

Target Market(s)

Upper Middle Class Adults who are progressively minded, artistic or artists, open to psychotherapy, interested in health & healing.

Industry/Entity Type

Business

Requirements
Must have
• Text to be included:

Lora Beckett
Counseling, Psychotherapy & Expressive Arts

2814 Wexford Avenue, Suite F
San Francisco, CA 94127
p. 415.862.3097
lorajanebeckett@mailvane.net

www.lorabeckettmft.com

MFT License Number 68947

It's OK to abbreviate Number to # or Street to St., etc.

Must be compatible with letter press printing.
Nice to have
• I don't have a logo. I don't expect designers to necessarily create one for me, but if someone comes up with a simple image (see above about flame), that would be great. I don't have much of a budget now, but expect that to change in the next year or so and then could buy a logo for my website, future letterhead, etc.

```html
<!DOCTYPE html>
<html lang="en">
<head>
<meta charset="utf-8">
<title>Lora Beckett Business Cards</title>
<link href="https://fonts.googleapis.com/css2?family=Open+Sans:wght@400;600;700&display=swap" rel="stylesheet">
<style>
  :root {
    --stage: #e9e9e9;
    --rose: #e03c57;
    --rose-light: #ea5f76;
    --paper: #ffffff;
    --slate: #6b6b6b;
    --ink-grey: #5a5a5a;
    --peach: #f0c9a4;
  }
  * { box-sizing: border-box; margin: 0; padding: 0; }
  html, body {
    width: 1200px;
    height: 861px;
    overflow: hidden;
  }
  body {
    background: var(--stage);
    font-family: "Open Sans", Arial, sans-serif;
  }
  .card-set {
    position: absolute;
    top: 282px;
    left: 60px;
    display: flex;
    gap: 40px;
  }
  .card {
    position: relative;
    width: 520px;
    height: 297px;
    padding: 42px 0 0 46px;
    box-shadow: 0 6px 18px rgba(0,0,0,0.18);
  }
  .card--rose {
    background: linear-gradient(135deg, var(--rose-light), var(--rose) 60%, #d3334f);
    color: var(--paper);
  }
  .card--paper {
    background: linear-gradient(135deg, var(--paper) 55%, #eeeeee);
    color: var(--ink-grey);
  }
  .card__name {
    font-size: 19px;
    font-weight: 700;
    letter-spacing: 0.2px;
    text-transform: uppercase;
    line-height: 1.1;
  }
  .card--paper .card__name { color: var(--rose); }
  .card__role {
    margin-top: 3px;
    font-size: 9.5px;
    font-weight: 700;
    text-transform: uppercase;
  }
  .contact-list {
    list-style: none;
    margin-top: 44px;
    display: flex;
    flex-direction: column;
    align-items: flex-start;
    gap: 7px;
  }
  .contact-list li {
    font-size: 10.5px;
    padding: 2px 5px;
    line-height: 1.35;
  }
  .card--rose .contact-list li { background: var(--paper); color: var(--rose); }
  .card--paper .contact-list li { background: var(--slate); color: var(--paper); }
  .logo-slot {
    position: absolute;
    right: 52px;
    top: 96px;
    width: 120px;
    height: 120px;
    border-radius: 50%;
  }
  .card--rose .logo-slot { background: rgba(255,255,255,0.85); }
  .card--paper .logo-slot { background: var(--rose); }
  .card__rule {
    position: absolute;
    left: 46px;
    right: 16px;
    bottom: 30px;
    height: 3px;
  }
  .card--rose .card__rule { background: var(--paper); }
  .card--paper .card__rule { background: var(--peach); }
</style>
</head>
<body>
  <main class="card-set">
    <section class="card card--rose">
      <h1 class="card__name">Lora Beckett</h1>
      <p class="card__role">Counseling, Psychotherapy &amp; Expressive Arts</p>
      <ul class="contact-list">
        <li>2814 Wexford Avenue, Suite F San Francisco, CA 94127</li>
        <li>415.862.3097</li>
        <li>lorajanebeckett@mailvane.net</li>
        <li>www.lorabeckettmft.com</li>
        <li>MFT License Number 68947</li>
      </ul>
      <div class="logo-slot" role="img" aria-label="Logo placeholder for Lora Beckett"></div>
      <div class="card__rule"></div>
    </section>

    <section class="card card--paper">
      <h2 class="card__name">Lora Beckett</h2>
      <p class="card__role">Counseling, Psychotherapy &amp; Expressive Arts</p>
      <ul class="contact-list">
        <li>2814 Wexford Avenue, Suite F San Francisco, CA 94127</li>
        <li>415.862.3097</li>
        <li>lorajanebeckett@mailvane.net</li>
        <li>www.lorabeckettmft.com</li>
        <li>MFT License Number 68947</li>
      </ul>
      <div class="logo-slot" role="img" aria-label="Logo placeholder for Lora Beckett"></div>
      <div class="card__rule"></div>
    </section>
  </main>
</body>
</html>
```